Pagecraft Design Project

I currently have a temporary website at www.brindlecroftadvisory.com this site provides a good sample of the information which needs to be included on the website. As you will see the design is very basic and does not include the company logo or any reference to the colors of the logo.

A couple of webpages which I really like and should provide an indication:
- quilvo.com
- tarravox.it (good client log in, dont like dark colors)
- pixel harbour
- lumatill.com

I have also added the company logo and my business card which provide some idea of coloring etc.

Requirements
Must have
• - Blog Page - see blog.quilvo.com for a good example;
- Client log-in;
- Twitter linkage;
- linkedin linkage;
- mobile browser scale ability;

```html
<!DOCTYPE html>
<html lang="en">
<head>
<meta charset="utf-8">
<title>Brindlecroft Partners – Consulting</title>
<link rel="stylesheet" href="https://fonts.googleapis.com/css2?family=Arimo:wght@400;700&family=Open+Sans:wght@400&family=Gelasio&display=swap">
<style>
  :root {
    --cyan: #1ab0d8;
    --cyan-soft: #a6dcea;
    --panel: #e6eff2;
    --menu: #e9f1f4;
    --text: #8a8a8a;
    --text-dark: #6f6f6f;
    --heading: #666a6e;
    --nav: #5a5a5a;
    --rule: #b9bcbf;
    --footer: #a3a8ae;
    --orange: #f7941d;
    --navy: #2f4d8c;
    --white: #ffffff;
    --placeholder: #f1f4f6;
  }
  * { box-sizing: border-box; margin: 0; padding: 0; }
  html, body { width: 904px; height: 1200px; overflow: hidden; }
  body {
    position: relative;
    background: var(--white);
    font-family: "Arimo", Arial, sans-serif;
    color: var(--text);
  }
  ul { list-style: none; }
  h1, h2, h3 { font-weight: 400; }

  /* Header */
  .site-header { position: absolute; top: 0; left: 0; width: 904px; height: 65px; }
  .brand { position: absolute; left: 105px; top: 12px; display: flex; align-items: center; gap: 8px; }
  .brand-dot { width: 38px; height: 38px; border-radius: 50%; background: var(--cyan); }
  .brand-name { font-family: "Gelasio", Georgia, serif; font-size: 20px; color: var(--navy); line-height: 22px; }
  .brand-tag { font-family: "Gelasio", Georgia, serif; font-size: 8.5px; letter-spacing: 3.2px; color: var(--navy); }
  .login-btn {
    position: absolute; left: 703px; top: 0; width: 93px; height: 21px;
    background: #8f949a; color: var(--white); border-radius: 0 0 3px 3px;
    font-size: 8px; display: flex; align-items: center; padding-left: 8px; gap: 8px;
  }
  .main-nav { position: absolute; right: 119px; top: 38px; display: flex; gap: 15px; }
  .main-nav a { font-size: 10.5px; font-weight: 700; color: var(--nav); text-decoration: none; }

  /* Hero */
  .hero { position: absolute; top: 65px; left: 0; width: 904px; height: 179px; }
  .hero-photo {
    position: absolute; inset: 0;
    background: linear-gradient(90deg, #e8eef3 0%, #d9e2ea 30%, #9fb8d6 55%, #5a82bd 80%, #3f68ac 100%);
  }
  .hero-card {
    position: absolute; left: 341px; top: 64px; width: 455px; height: 115px;
    background: var(--white); border-radius: 14px 0 0 0; padding: 24px 0 0 14px;
  }
  .hero-title { font-family: "Open Sans", Verdana, sans-serif; font-weight: 400; font-size: 28px; color: var(--cyan); line-height: 34px; }
  .hero-sub { font-family: "Open Sans", Verdana, sans-serif; font-size: 12.5px; color: var(--text); margin-top: 5px; }

  /* Sidebar */
  .sidebar { position: absolute; left: 105px; top: 250px; width: 195px; }
  .side-title { font-family: "Open Sans", Verdana, sans-serif; font-weight: 400; font-size: 18px; color: var(--cyan); }
  .side-menu { margin-top: 5px; }
  .side-menu li {
    height: 32px; margin-bottom: 4px; border-radius: 0 8px 8px 0; background: var(--menu);
    font-size: 12px; color: var(--text); padding: 9px 8px;
  }
  .side-menu li.is-active { background: var(--cyan-soft); color: var(--white); }

  .blog-card { position: absolute; left: 105px; top: 452px; width: 188px; height: 334px; background: var(--panel); }
  .blog-title { position: absolute; left: 6px; top: 9px; font-family: "Open Sans", Verdana, sans-serif; font-weight: 400; font-size: 20px; color: var(--cyan); }
  .blog-image {
    position: absolute; left: 6px; top: 48px; width: 175px; height: 183px;
    background: var(--placeholder);
  }
  .blog-date {
    position: absolute; left: 131px; top: 14px; width: 56px; height: 56px; border-radius: 50%;
    background: var(--orange); color: var(--white); font-family: "Gelasio", Georgia, serif;
    font-size: 14px; display: flex; align-items: center; justify-content: center;
  }
  .blog-excerpt { position: absolute; left: 8px; top: 263px; width: 170px; font-size: 11.5px; line-height: 13.5px; color: var(--text-dark); }
  .blog-more { position: absolute; left: 8px; top: 314px; font-size: 9px; font-weight: 700; color: var(--cyan); }

  /* Main content */
  .content { position: absolute; left: 341px; top: 0; width: 455px; }
  .breadcrumb { position: absolute; top: 254px; left: 0; width: 455px; height: 20px; border-bottom: 1px solid var(--rule); font-size: 11px; color: var(--text); }
  .breadcrumb .current { color: var(--cyan); }
  .service { position: absolute; left: 0; width: 455px; }
  .service h2 { font-family: "Open Sans", Verdana, sans-serif; font-weight: 400; font-size: 24px; color: var(--heading); line-height: 30px; margin-bottom: 4px; }
  .service p { font-size: 8.6px; line-height: 12.8px; color: var(--text); margin-bottom: 12px; }
  .points { background: var(--panel); padding: 2px 0 2px 8px; margin: -2px 0 12px; }
  .points li { height: 22.3px; display: flex; align-items: center; gap: 7px; font-size: 9.5px; color: var(--text-dark); }
  .points svg { flex: none; }

  /* Footer */
  .site-footer { position: absolute; left: 0; top: 1086px; width: 904px; height: 114px; background: var(--footer); color: var(--white); }
  .footer-brand { position: absolute; left: 105px; top: 20px; display: flex; align-items: center; gap: 6px; font-size: 16px; font-weight: 700; }
  .footer-brand span.square { width: 16px; height: 16px; background: var(--white); }
  .copyright { position: absolute; left: 105px; top: 70px; font-size: 8px; }
  .footer-nav { position: absolute; right: 117px; top: 14px; display: flex; gap: 16px; }
  .footer-nav a { font-size: 10.5px; font-weight: 700; color: var(--white); text-decoration: none; }
  .newsletter { position: absolute; left: 489px; top: 50px; width: 190px; height: 22px; background: var(--white); border: 3px solid #c7cbcf; font-size: 8px; color: var(--text); padding: 4px 12px; }
  .newsletter svg { position: absolute; right: 10px; top: 3px; }
  .social { position: absolute; left: 684px; top: 50px; display: flex; gap: 5px; }
  .social li { width: 24px; height: 24px; background: #c1c5c9; }
  .footer-note { position: absolute; left: 489px; top: 80px; font-size: 7.5px; }
</style>
</head>
<body>
  <header class="site-header">
    <div class="brand">
      <span class="brand-dot"></span>
      <div>
        <div class="brand-name">Brindlecroft Partners</div>
        <div class="brand-tag">Business Advisors</div>
      </div>
    </div>
    <div class="login-btn">Customer Log In
      <svg width="7" height="11" viewBox="0 0 7 11"><path d="M1 1l4.5 4.5L1 10" fill="none" stroke="#fff" stroke-width="1.6"/></svg>
    </div>
    <nav class="main-nav">
      <a href="#">Home</a><a href="#">Consulting</a><a href="#">Accounting</a><a href="#">Blog</a><a href="#">Partners</a><a href="#">About Us</a><a href="#">Contact Us</a>
    </nav>
  </header>

  <section class="hero">
    <div class="hero-photo" role="img" aria-label="Photo of a business team meeting around a table in a bright office"></div>
    <div class="hero-card">
      <h1 class="hero-title">Consulting</h1>
      <p class="hero-sub">Lorem Ipsum is simply dummy text of the printing</p>
    </div>
  </section>

  <aside class="sidebar">
    <h3 class="side-title">Navigate</h3>
    <ul class="side-menu">
      <li class="is-active">Consulting</li>
      <li>Accounting</li>
      <li>Partners</li>
      <li>About Us</li>
    </ul>
  </aside>

  <aside class="blog-card">
    <h3 class="blog-title">Our Blog</h3>
    <div class="blog-image" role="img" aria-label="Blog post illustration"></div>
    <div class="blog-date">May 6</div>
    <p class="blog-excerpt">People love their fans. They love to set them on timers, to schedule them to…</p>
    <span class="blog-more">More &nbsp;<svg width="6" height="8" viewBox="0 0 6 8"><path d="M1 1l3 3-3 3" fill="none" stroke="#1ab0d8" stroke-width="1.5"/></svg></span>
  </aside>

  <main class="content">
    <div class="breadcrumb">Navigate &nbsp;<svg width="6" height="8" viewBox="0 0 6 8"><path d="M1 1l3 3-3 3" fill="none" stroke="#8a8a8a" stroke-width="1"/></svg>&nbsp; <span class="current">Consulting</span></div>

    <section class="service" style="top:283px">
      <h2>Turn Around</h2>
      <p>Often external factors can result in a business being at risk of failure. In these situations Brindlecroft Partners are well qualified to identify the critical issues faced by businesses and can provide assistance in resolving these issues. Through assessing the position of the business we can prepare a plan for the business to move forward.</p>
      <ul class="points">
        <li><svg width="6" height="8" viewBox="0 0 6 8"><path d="M1 1l3 3-3 3" fill="none" stroke="#1ab0d8" stroke-width="1.6"/></svg>Negotiation with NTA</li>
        <li><svg width="6" height="8" viewBox="0 0 6 8"><path d="M1 1l3 3-3 3" fill="none" stroke="#1ab0d8" stroke-width="1.6"/></svg>Cash flow management</li>
        <li><svg width="6" height="8" viewBox="0 0 6 8"><path d="M1 1l3 3-3 3" fill="none" stroke="#1ab0d8" stroke-width="1.6"/></svg>Finance and working capital</li>
        <li><svg width="6" height="8" viewBox="0 0 6 8"><path d="M1 1l3 3-3 3" fill="none" stroke="#1ab0d8" stroke-width="1.6"/></svg>Accounting processes</li>
        <li><svg width="6" height="8" viewBox="0 0 6 8"><path d="M1 1l3 3-3 3" fill="none" stroke="#1ab0d8" stroke-width="1.6"/></svg>Business processes</li>
      </ul>
    </section>

    <section class="service" style="top:493px">
      <h2>Due Diligence</h2>
      <p>Financial transactions invariably require a level of due diligence, this process covers a range of areas, including but not limited to:</p>
      <ul class="points">
        <li><svg width="6" height="8" viewBox="0 0 6 8"><path d="M1 1l3 3-3 3" fill="none" stroke="#1ab0d8" stroke-width="1.6"/></svg>Operational Due Diligence;</li>
        <li><svg width="6" height="8" viewBox="0 0 6 8"><path d="M1 1l3 3-3 3" fill="none" stroke="#1ab0d8" stroke-width="1.6"/></svg>Legal Due Diligence;</li>
        <li><svg width="6" height="8" viewBox="0 0 6 8"><path d="M1 1l3 3-3 3" fill="none" stroke="#1ab0d8" stroke-width="1.6"/></svg>Financial Due Diligence;</li>
      </ul>
      <p>The scope of these works will vary between transactions. Brindlecroft Partners can assist you through this process, providing specific advice in relation to financial due diligence and providing guidance with legal and operational due diligence.</p>
    </section>

    <section class="service" style="top:693px">
      <h2>Structuring</h2>
      <p>Choosing the right structure, is critical to the long-term effectiveness and efficiencies of a business or transaction. Getting it wrong can have serious tax and asset protection ramifications.</p>
      <p>We provide advice based upon a strong understanding of the business and/or transaction. This will ensure that we provide a solution which mitigates the risks as identified.</p>
    </section>

    <section class="service" style="top:809px">
      <h2>Solvency Support</h2>
      <p>We provide businesses and individuals facing financial difficulties with independent impartial advice. With a wealth of experience in restructuring, refinancing and successful asset divestments, we can help guide a business through what can be very difficult time for businesses and business owners. This advice may include:</p>
      <ul class="points">
        <li><svg width="6" height="8" viewBox="0 0 6 8"><path d="M1 1l3 3-3 3" fill="none" stroke="#1ab0d8" stroke-width="1.6"/></svg>Assisting directors understand solvency and their obligations;</li>
        <li><svg width="6" height="8" viewBox="0 0 6 8"><path d="M1 1l3 3-3 3" fill="none" stroke="#1ab0d8" stroke-width="1.6"/></svg>Preparing providing directors independent advice through an administration process;</li>
        <li><svg width="6" height="8" viewBox="0 0 6 8"><path d="M1 1l3 3-3 3" fill="none" stroke="#1ab0d8" stroke-width="1.6"/></svg>Providing directors with formal insolvency options available;</li>
        <li><svg width="6" height="8" viewBox="0 0 6 8"><path d="M1 1l3 3-3 3" fill="none" stroke="#1ab0d8" stroke-width="1.6"/></svg>Designing a Deed of Company arrangement or other informal arrangement.</li>
      </ul>
      <p>With significant experience with business valuation, we tailor a valuation to suit your needs. We ensure that the reports are written in plain English and our methodology is fully explained, this enables the users to fully understand the process.</p>
    </section>
  </main>

  <footer class="site-footer">
    <div class="footer-brand"><span class="square"></span>Brindlecroft</div>
    <div class="copyright">© 2013 Brindlecroft Partners</div>
    <nav class="footer-nav">
      <a href="#">Home</a><a href="#">Consulting</a><a href="#">Accounting</a><a href="#">Blog</a><a href="#">Partners</a><a href="#">About Us</a><a href="#">Contact Us</a>
    </nav>
    <div class="newsletter">Enter email
      <svg width="10" height="10" viewBox="0 0 10 10"><circle cx="5" cy="5" r="4.3" fill="none" stroke="#b0b0b0"/><path d="M4 3l2 2-2 2" fill="none" stroke="#b0b0b0"/></svg>
    </div>
    <ul class="social"><li></li><li></li><li></li><li></li></ul>
    <div class="footer-note">Private, secure, spam-free.</div>
  </footer>
</body>
</html>
```